Flyer to advertise gutter cleaning throughout the Autumn and winter monthss

I need a new flyer to advertise gutter and driveway cleaning, roof and gutter repairs.

I am an experienced licensed Plumber and Gasfitter looking to broaden my scope of work to gutter cleaning. I am experienced in cleaning gutter and live in a area with large gum trees. I wont something that's clear, eye catching but not too busy.

Flyer requirements: Free roof inspection - no obligation. Gutter Cleaning from $199. Pictures of men using blower or hands to clean roof gutters (no obvious faces) to be included. Australian looking houses.

A mention that 'All general plumbing maintenance' is offered as other services but not too much wording about this as the target is for gutter cleaning.

Phone number: 0437 582 316 (in this format)
Business Name: Bracken Plumbing & Gasfitting
License: 3817502
ABN: 71395046287
Web: http://brackenplumbing.example-site.net/

Target Market(s)

Elderly - busy working class

Industry/Entity Type

Plumber

Font styles to use
Sans Serif

Colors
0355a3
fbed22
ec1f27
f78f20

Requirements
Must have
• Roof Gutter Cleaning pictures
• Men in protective clothing if possible
Nice to have
• More information:
• Prevent against flooding, mold, rust, rotting and corrosion now!
• Gutter Cleaning Services
• • Remove leaves, sticks, and other debris
• • Clear away clogs
• • Test your downpipes
• • Pinpoint any gutter issues
• • Repair gutter
• With regular service, you can count on your property to be well-protected no matter what the forecast!
Should not have
• Houses that don't look Australian

```html
<!DOCTYPE html>
<html lang="en">
<head>
<meta charset="utf-8">
<title>Bracken Plumbing &amp; Gasfitting – Gutter Cleaning Flyer</title>
<link href="https://fonts.googleapis.com/css2?family=Lato:wght@300;400;700;900&display=swap" rel="stylesheet">
<style>
  :root {
    --red: #e60e3c;
    --navy: #1b3a8c;
    --bar-blue: #13318f;
    --panel-grey: #efefef;
    --white: #ffffff;
    --ink: #1e1e1e;
    --backdrop: #a4a4a4;
  }
  html, body {
    margin: 0;
    padding: 0;
    width: 1200px;
    height: 1200px;
    overflow: hidden;
    background: var(--backdrop);
    font-family: "Lato", Arial, sans-serif;
  }
  .flyer {
    position: absolute;
    left: 172px;
    top: 0;
    width: 908px;
    height: 1272px;
    background: var(--white);
    transform: scale(0.9434);
    transform-origin: 0 0;
    overflow: hidden;
  }
  .hero, .footer-art {
    position: absolute;
    left: 0;
    top: 0;
  }
  .brand {
    position: absolute;
    top: 464px;
    left: 0;
    width: 908px;
    height: 192px;
    display: flex;
    align-items: center;
    justify-content: center;
    gap: 22px;
  }
  .brand-dot {
    width: 110px;
    height: 110px;
    border-radius: 50%;
    border: 16px solid var(--navy);
    box-sizing: border-box;
  }
  .brand-name {
    font-weight: 700;
    font-size: 28px;
    color: var(--ink);
    letter-spacing: -0.3px;
  }
  .prices {
    position: absolute;
    top: 656px;
    left: 0;
    width: 908px;
    height: 226px;
    background: var(--panel-grey);
    display: flex;
  }
  .price-col {
    flex: 1;
    text-align: center;
    padding-top: 22px;
  }
  .price-col + .price-col {
    border-left: 2px solid #dcdcdc;
  }
  .divider-space { margin: 0; }
  .price-title {
    margin: 0;
    font-weight: 700;
    font-size: 35px;
    line-height: 43px;
    color: var(--navy);
  }
  .price-tag {
    display: inline-block;
    margin-top: 18px;
    width: 215px;
    height: 72px;
    box-sizing: border-box;
    background: var(--red);
    padding: 8px 9px;
    box-shadow: 0 8px 8px -4px rgba(0,0,0,0.35);
  }
  .price-tag span {
    display: block;
    height: 100%;
    border: 1.5px dashed rgba(255,255,255,0.85);
    box-sizing: border-box;
    color: var(--white);
    font-weight: 900;
    font-size: 46px;
    line-height: 52px;
  }
  .offer {
    position: absolute;
    left: 478px;
    top: 920px;
  }
  .offer-free {
    margin: 0;
    color: var(--red);
    font-weight: 900;
    font-size: 92px;
    line-height: 92px;
    letter-spacing: 2px;
    padding-left: 6px;
  }
  .offer-line {
    display: flex;
    align-items: center;
    margin-top: 12px;
  }
  .chip {
    color: var(--white);
    font-weight: 400;
    font-size: 44px;
    line-height: 48px;
    padding: 0 10px;
  }
  .chip-blue { background: var(--navy); }
  .chip-red { background: var(--red); }
  .offer-word {
    color: var(--navy);
    font-weight: 700;
    font-size: 36px;
    margin-left: 8px;
  }
  .offer-no {
    color: var(--navy);
    font-weight: 900;
    font-size: 56px;
    line-height: 52px;
    margin-right: 16px;
  }
  .offer-name {
    position: absolute;
    left: 454px;
    width: 372px;
    top: 1172px;
    text-align: center;
    color: var(--navy);
    font-weight: 700;
    font-size: 20px;
  }
  .rule-red {
    position: absolute;
    left: 454px;
    top: 1208px;
    width: 372px;
    height: 4px;
    background: var(--red);
  }
  .contact-bar {
    position: absolute;
    left: 400px;
    top: 1216px;
    height: 56px;
    display: flex;
    align-items: center;
    gap: 28px;
    color: var(--white);
    font-size: 16px;
  }
  .contact-phone {
    display: flex;
    align-items: center;
    gap: 6px;
    font-weight: 700;
    font-size: 20px;
  }
</style>
</head>
<body>
  <main class="flyer">
    <svg class="hero" width="908" height="464" viewBox="0 0 908 464">
      <defs>
        <linearGradient id="gutterPhoto" x1="0" y1="0" x2="1" y2="1">
          <stop offset="0" stop-color="#b9703f"/>
          <stop offset="0.45" stop-color="#7a5532"/>
          <stop offset="0.75" stop-color="#8f8a55"/>
          <stop offset="1" stop-color="#4a3a2c"/>
        </linearGradient>
      </defs>
      <polygon points="0,0 210,0 0,414" fill="var(--red)"/>
      <polygon points="258,0 908,0 908,10 672,464 22,464" fill="url(#gutterPhoto)" role="img" aria-label="Photo: gloved hand clearing dry leaves from a roof gutter beside terracotta tiles"/>
      <polygon points="908,66 716,464 908,464" fill="var(--bar-blue)"/>
    </svg>

    <header class="brand">
      <div class="brand-dot"></div>
      <div class="brand-name">BRACKEN PLUMBING &amp; GASFITTING</div>
    </header>

    <section class="prices">
      <div class="price-col">
        <h2 class="price-title">GUTTER CLEANING<br>FROM</h2>
        <div class="price-tag"><span>$199</span></div>
      </div>
      <div class="price-col">
        <h2 class="price-title">DRIVEWAY CLEANING<br>FROM</h2>
        <div class="price-tag"><span>$299</span></div>
      </div>
    </section>

    <svg class="footer-art" width="908" height="1272" viewBox="0 0 908 1272">
      <defs>
        <linearGradient id="drivewayPhoto" x1="0" y1="0" x2="1" y2="1">
          <stop offset="0" stop-color="#c8372f"/>
          <stop offset="0.35" stop-color="#6f5a58"/>
          <stop offset="0.7" stop-color="#8a6e6a"/>
          <stop offset="1" stop-color="#a9a39c"/>
        </linearGradient>
      </defs>
      <polygon points="0,903 462,903 282,1272 0,1272" fill="url(#drivewayPhoto)" role="img" aria-label="Photo: worker in rubber boots pressure-washing a driveway in front of a red garage door"/>
      <polygon points="423,1020 435,1020 314,1272 302,1272" fill="var(--bar-blue)"/>
      <polygon points="384,1216 908,1216 908,1272 355,1272" fill="var(--bar-blue)"/>
    </svg>

    <section class="offer">
      <p class="offer-free">FREE</p>
      <div class="offer-line">
        <span class="chip chip-blue">Roof</span>
        <span class="offer-word">INSPECTION</span>
      </div>
      <div class="offer-line" style="margin-top:24px">
        <span class="offer-no">NO</span>
        <span class="chip chip-red">Obligation</span>
      </div>
    </section>

    <div class="offer-name">Bracken Plumbing &amp; Gasfitting</div>
    <div class="rule-red"></div>

    <footer class="contact-bar">
      <span class="contact-phone">
        <svg width="18" height="18" viewBox="0 0 24 24" aria-hidden="true"><path fill="#fff" d="M6.6 10.8a15.1 15.1 0 0 0 6.6 6.6l2.2-2.2a1 1 0 0 1 1-.25 11.4 11.4 0 0 0 3.6.57 1 1 0 0 1 1 1V20a1 1 0 0 1-1 1A17 17 0 0 1 3 4a1 1 0 0 1 1-1h3.5a1 1 0 0 1 1 1c0 1.25.2 2.45.57 3.6a1 1 0 0 1-.25 1z"/></svg>
        0437 582 316
      </span>
      <span>License: 3817502</span>
      <span>ABN: 71395046287</span>
    </footer>
  </main>
</body>
</html>
```